Business Card Design

Stronger Care Network for the Riverlands is a partnership of twenty different health organisations in the western suburbs of Melbourne, working together to improve the health of the local community. The western suburbs of Melbourne is one of the fastest growing and most culturally diverse populations in Australia and its communities have some of the poorest health outcomes in Australia.
Please see location for copy of the SCNR:
http://qvlr.com.au/fileadmin/filemount/pdf_files/SCNFTR_13_FINAL_JUNE_2012.pdf
Updates

Reason: Hello. I've extended the deadline because in the brief I made a confusing mention about a logo, but I actually meant the 'Stronger Care Network for the Riverlands' jpg that I had already attached. Sorry about the confusion Thanks Rosalind

Hello, Thanks for the designs I have already received. I have extended the deadline because I made a confusing reference to a logo in my brief, but I was talking about the 'Stronger Care Network for the Riverlands' jpg I had already attached. There is no other logo for me to provide.

Thanks, Rosalind

Target Market(s)

Health and state/local government managers and CEOs

Industry/Entity Type

Health

Contact Information for Business Card

Rosalind Tiernan
Executive Officer
Stronger Care Network for the Riverlands
Ph: 0438 295 614
Rosalind.Tiernan@kp.org.au

Requirements
Must have
• logo and details as provided.
Would prefer matt finish
I can't see that logo has successfully attached so if it has not, please email or call me to follow up.

```html
<!DOCTYPE html>
<html lang="en">
<head>
<meta charset="utf-8">
<title>Stronger Care Network for the Riverlands – Business Card</title>
<link rel="stylesheet" href="https://fonts.googleapis.com/css2?family=Lato:wght@300;400;700;900&display=swap">
<style>
  :root {
    --brand-blue: #1a8ccc;
    --brand-blue-deep: #137cbc;
    --paper: #ffffff;
    --paper-tint: #eef3f9;
    --stage: #e4e4e4;
  }
  * { box-sizing: border-box; margin: 0; padding: 0; }
  html, body {
    width: 1200px;
    height: 750px;
    overflow: hidden;
  }
  body {
    background: var(--stage);
    font-family: "Lato", sans-serif;
    display: flex;
    align-items: center;
    justify-content: center;
    gap: 60px;
  }
  .card {
    position: relative;
    width: 500px;
    height: 286px;
    border-radius: 26px;
    overflow: hidden;
    box-shadow: 0 6px 18px rgba(0, 0, 0, 0.18);
  }
  .card__art {
    position: absolute;
    inset: 0;
    width: 100%;
    height: 100%;
  }

  /* Shared brand name mark */
  .brand-mark {
    display: flex;
    align-items: center;
    gap: 6px;
    color: var(--brand-blue);
    font-weight: 900;
    letter-spacing: 0.04em;
    line-height: 1;
  }
  .brand-mark__dot {
    display: block;
    border-radius: 50%;
    background: var(--brand-blue);
  }

  /* Front: personal details */
  .card--front { background: var(--brand-blue); }
  .card--front .brand-mark {
    position: absolute;
    top: 78px;
    left: 270px;
    font-size: 13px;
  }
  .card--front .brand-mark__dot { width: 11px; height: 11px; }
  .identity {
    position: absolute;
    top: 98px;
    right: 34px;
    text-align: right;
    color: var(--brand-blue);
  }
  .identity__name {
    font-weight: 900;
    font-size: 33px;
    letter-spacing: 0.01em;
    line-height: 1;
    text-transform: uppercase;
  }
  .identity__role {
    margin-top: 6px;
    font-weight: 400;
    font-size: 10px;
    letter-spacing: 0.06em;
    text-transform: uppercase;
  }
  .identity__org {
    margin-top: 2px;
    font-weight: 700;
    font-size: 9.5px;
    letter-spacing: 0.03em;
    text-transform: uppercase;
  }
  .contact {
    position: absolute;
    top: 204px;
    left: 0;
    right: 0;
    text-align: center;
    color: var(--paper);
    font-weight: 300;
    font-size: 11px;
    letter-spacing: 0.08em;
    text-transform: uppercase;
  }
  .contact__line { display: block; line-height: 1.35; }
  .contact__rule {
    display: block;
    width: 170px;
    height: 1px;
    margin: 3px auto;
    background: rgba(255, 255, 255, 0.7);
  }

  /* Back: brand side */
  .card--back { background: var(--paper); }
  .card--back .brand-mark {
    position: absolute;
    top: 110px;
    left: 0;
    right: 0;
    justify-content: center;
    font-size: 30px;
  }
  .card--back .brand-mark__dot { width: 22px; height: 22px; }
  .brand-line {
    position: absolute;
    top: 172px;
    left: 0;
    right: 0;
    text-align: center;
    color: var(--brand-blue);
    font-weight: 700;
    font-size: 14px;
    letter-spacing: 0.02em;
    text-transform: uppercase;
  }
</style>
</head>
<body>

  <article class="card card--front">
    <svg class="card__art" viewBox="0 0 500 286" aria-hidden="true">
      <path d="M-20 260 C 80 120, 220 60, 380 -20" fill="none" stroke="#ffffff" stroke-opacity="0.12" stroke-width="40"/>
      <path d="M120 300 C 200 200, 340 150, 520 140" fill="none" stroke="#ffffff" stroke-opacity="0.08" stroke-width="30"/>
      <rect x="0" y="68" width="500" height="124" fill="#ffffff"/>
    </svg>
    <div class="brand-mark"><span class="brand-mark__dot"></span>SCNR</div>
    <div class="identity">
      <h1 class="identity__name">Rosalind Tiernan</h1>
      <p class="identity__role">Executive Officer</p>
      <p class="identity__org">Stronger Care Network for the Riverlands</p>
    </div>
    <p class="contact">
      <span class="contact__line">Ph: 0438 295 614</span>
      <span class="contact__rule"></span>
      <span class="contact__line">Rosalind.Tiernan@kp.org.au</span>
    </p>
  </article>

  <article class="card card--back">
    <svg class="card__art" viewBox="0 0 500 286" aria-hidden="true">
      <path d="M360 -10 C 470 40, 520 200, 440 300 L 520 300 L 520 -10 Z" fill="#eef3f9"/>
      <path d="M410 -10 C 500 40, 530 180, 470 300 L 520 300 L 520 -10 Z" fill="#1a8ccc"/>
      <path d="M-10 140 C 60 230, 160 260, 240 300 L -10 300 Z" fill="#eef3f9"/>
      <path d="M-10 250 C 40 270, 80 280, 130 300 L -10 300 Z" fill="#1a8ccc"/>
    </svg>
    <div class="brand-mark"><span class="brand-mark__dot"></span>SCNR</div>
    <p class="brand-line">Stronger Care Network for the Riverlands</p>
  </article>

</body>
</html>
```